Prayer Service 12.28.2013

I need a flyer designed for a Christian prayer service. The title and theme is:
"Total and Complete Surrender for Total and Complete Deliverance!"
1. You have creative freedom with imagery and typography
2. I need a quick turnaround time
FLYER DETAILS:
A prayer, anointing, and deliverance all night prayer service, at Brightwater Assembly.
Saturday December 28 2013 from 9pm-6am.
Special guest speakers, prayer,anointing,and deliverance sessions.
For more information contact Sis Dorothy Whitfield at Brightwater Assembly 555 634 1297 Ext. 4816 or Monica Shaw at 555 802-3941

```html
<!DOCTYPE html>
<html lang="en">
<head>
<meta charset="utf-8">
<title>Total and Complete Surrender — All Night Prayer Service</title>
<link rel="stylesheet" href="https://fonts.googleapis.com/css2?family=Kalam:wght@700&family=Ultra&family=Cinzel:wght@600&family=Carlito:wght@400;700&display=swap">
<style>
  :root {
    --sky-top: #5f9a9c;
    --sky-mid: #8cbcbc;
    --sky-light: #c9dcd6;
    --cloud: #f3ead6;
    --band: #1b3560;
    --title-ink: #1d3f73;
    --glow-white: #ffffff;
    --caps-ink: #d9f1f7;
    --caps-glow: #6fc4d6;
    --tagline: #d7d9dc;
    --footer: #a9b6c8;
  }
  html, body {
    margin: 0;
    padding: 0;
    overflow: hidden;
    background: #ffffff;
  }
  .flyer {
    position: relative;
    width: 927px;
    height: 1200px;
    overflow: hidden;
    background: var(--band);
  }
  .sky {
    position: absolute;
    left: 0;
    top: 0;
    width: 927px;
    height: 934px;
    background:
      radial-gradient(ellipse 70% 45% at 72% 78%, var(--cloud) 0%, rgba(243,234,214,0.6) 35%, rgba(243,234,214,0) 70%),
      radial-gradient(ellipse 60% 35% at 25% 88%, rgba(240,230,205,0.9) 0%, rgba(240,230,205,0) 70%),
      radial-gradient(ellipse 80% 40% at 55% 40%, rgba(210,228,222,0.7) 0%, rgba(210,228,222,0) 70%),
      linear-gradient(180deg, var(--sky-top) 0%, var(--sky-mid) 45%, var(--sky-light) 80%, #e6e2d2 100%);
  }
  .sky-fade {
    position: absolute;
    left: 0;
    top: 900px;
    width: 927px;
    height: 40px;
    background: linear-gradient(180deg, rgba(27,53,96,0) 0%, var(--band) 100%);
  }
  .title {
    position: absolute;
    left: 0;
    top: 30px;
    width: 927px;
    margin: 0;
    text-align: center;
    font-family: "Kalam", cursive;
    font-weight: 700;
    font-size: 52px;
    line-height: 80px;
    letter-spacing: 1px;
    text-transform: uppercase;
    color: var(--title-ink);
    text-shadow: 0 0 3px var(--glow-white), 0 0 8px var(--glow-white), 0 2px 4px rgba(255,255,255,0.9);
  }
  .when {
    position: absolute;
    left: 0;
    top: 312px;
    width: 927px;
    text-align: center;
    font-family: "Ultra", serif;
    font-size: 36px;
    line-height: 49px;
    color: #ffffff;
    text-shadow: 0 0 4px rgba(120,150,170,0.9), 0 0 10px rgba(120,160,180,0.7);
  }
  .service {
    position: absolute;
    left: 0;
    top: 437px;
    width: 927px;
    margin: 0;
    padding: 0;
    list-style: none;
    text-align: center;
    font-family: "Cinzel", serif;
    font-weight: 600;
    font-size: 36px;
    line-height: 84px;
    letter-spacing: 5px;
    text-transform: uppercase;
    color: var(--caps-ink);
    text-shadow: 0 0 4px var(--caps-glow), 0 0 10px var(--caps-glow), 0 0 2px #3b7d90;
  }
  .tagline {
    position: absolute;
    left: 0;
    top: 955px;
    width: 927px;
    margin: 0;
    text-align: center;
    font-family: "Carlito", sans-serif;
    font-weight: 700;
    font-size: 49px;
    line-height: 77px;
    color: var(--tagline);
    text-shadow: 0 2px 3px rgba(0,0,0,0.35);
  }
  .contact {
    position: absolute;
    left: 0;
    top: 1132px;
    width: 927px;
    margin: 0;
    text-align: center;
    font-family: "Carlito", sans-serif;
    font-size: 14.5px;
    line-height: 23px;
    color: var(--footer);
  }
</style>
</head>
<body>
<main class="flyer">
  <div class="sky" role="img" aria-label="Photograph of a soft blue-green sky with sunlit white clouds and light rays"></div>
  <div class="sky-fade"></div>

  <h1 class="title">Total and Complete Surrender<br>for Total and Complete<br>Deliverance</h1>

  <p class="when" style="margin:0">Saturday, December 28, 2013<br>9 p.m. – 6 a.m.</p>

  <ul class="service">
    <li>A Prayer,</li>
    <li>Anointing,</li>
    <li>and Deliverance</li>
    <li>All Night Prayer Service</li>
    <li>at Brightwater</li>
    <li>Assembly</li>
  </ul>

  <p class="tagline">Special guest speakers, prayer,<br>anointing, and deliverance sessions.</p>

  <p class="contact">For more information contact Sis Dorothy Whitfield at Brightwater Assembly (555) 634-1297 Ext. 4816<br>or Monica Shaw at (555) 802-3941</p>
</main>
</body>
</html>
```